More Chiropractic Certificates to Change to LM JPEGs

This is a set of postcards that I want to convert into colored JPEGs with more modern graphics and colors than these black and white images so that they would be suitable to post on Lumorra. The cards have a front and back that would be combined into the same image so that it will work as a LM post. The back of the card is file m169. For LM I would change it to...
"Who do you know who could benefit from our care? Share this message with them and we will give them a complete Consultation and Examination at no charge."
The cards are for several seasons: New Years (m173), Valentines Day (m181-182), USA Independence Day (m170-172) and Thanksgiving (m177-179), Spring (m174-176). You'll see that each season has a similar look with a quote that changes. So, I'd like a seasonal look for each group, featuring the quotation that changes each time with the offer below the quotation. "Care enough to Share" should be the headline for each certificate, followed by the quotation, followed by "Who do you know who could benefit from our care? Share this message with them and we will give them a complete Consultation and Examination at no charge."

```html
<!DOCTYPE html>
<html lang="en">
<head>
<meta charset="utf-8">
<title>Care Enough To Share – Thanksgiving Card Sheet</title>
<link href="https://fonts.googleapis.com/css2?family=Tinos:ital,wght@0,400;0,700;1,400;1,700&display=swap" rel="stylesheet">
<style>
  :root {
    --sheet: #ffffff;
    --card-edge: #f6d46a;
    --card-glow: #fffbe8;
    --headline-red: #d8322a;
    --badge-blue: #1c9ad8;
    --badge-text: #ffffff;
    --quote-navy: #2e2878;
    --fruit-a: #f4c430;
    --fruit-b: #8cc63f;
    --fruit-c: #e8452c;
    --trim-mark: #c8323a;
  }
  html, body {
    margin: 0;
    padding: 0;
    width: 773px;
    height: 1200px;
    overflow: hidden;
    background: var(--sheet);
  }
  .sheet {
    position: relative;
    width: 773px;
    height: 1200px;
    font-family: "Tinos", "Times New Roman", serif;
  }
  .trim-marks {
    position: absolute;
    inset: 0;
  }
  .card {
    position: absolute;
    left: 43px;
    width: 687px;
    height: 510px;
    background: radial-gradient(ellipse 60% 65% at 52% 52%, var(--card-glow) 0%, #fdf0b8 55%, var(--card-edge) 100%);
    overflow: hidden;
  }
  .card--top { top: 43px; }
  .card--bottom { top: 642px; }
  .headline {
    position: absolute;
    margin: 0;
    font-weight: 700;
    color: var(--headline-red);
    font-size: 60px;
    line-height: 1;
  }
  .headline--care { left: 44px; top: 54px; }
  .headline--share { left: 44px; top: 272px; }
  .badge {
    position: absolute;
    left: 40px;
    top: 115px;
    width: 299px;
    height: 126px;
    background: var(--badge-blue);
    border-radius: 12px;
    display: flex;
    align-items: center;
    justify-content: center;
    color: var(--badge-text);
    font-style: italic;
    font-weight: 700;
    font-size: 72px;
    line-height: 1;
    padding-bottom: 8px;
    box-sizing: border-box;
  }
  .fruit-art {
    position: absolute;
    left: 378px;
    top: 72px;
    width: 259px;
    height: 146px;
    border-radius: 40px;
    background: linear-gradient(110deg, var(--fruit-c) 0%, var(--fruit-a) 45%, var(--fruit-b) 70%, var(--fruit-a) 100%);
    opacity: 0.85;
  }
  .season {
    position: absolute;
    left: 383px;
    top: 228px;
    margin: 0;
    font-style: italic;
    font-weight: 700;
    font-size: 35px;
    color: var(--headline-red);
    line-height: 1;
  }
  .quote {
    position: absolute;
    left: 57px;
    top: 345px;
    margin: 0;
    font-style: italic;
    font-weight: 700;
    font-size: 34px;
    line-height: 41px;
    color: var(--quote-navy);
  }
  .quote-author {
    position: absolute;
    right: 65px;
    top: 421px;
    margin: 0;
    font-style: italic;
    font-size: 14px;
    line-height: 1;
    color: var(--headline-red);
  }
  .offer {
    position: absolute;
    left: 57px;
    width: 580px;
    top: 446px;
    margin: 0;
    font-size: 16px;
    line-height: 20px;
    color: var(--quote-navy);
  }
</style>
</head>
<body>
<div class="sheet">
  <svg class="trim-marks" width="773" height="1200" viewBox="0 0 773 1200" aria-hidden="true">
    <g stroke="var(--trim-mark)" stroke-width="1.2" fill="none">
      <path d="M43 0v30 M0 43h30 M730 0v30 M743 43h30"/>
      <path d="M43 566v30 M0 553h30 M730 566v30 M743 553h30"/>
      <path d="M43 600v30 M0 642h30 M730 600v30 M743 642h30"/>
      <path d="M43 1166v34 M0 1153h30 M730 1166v34 M743 1153h30"/>
    </g>
  </svg>

  <section class="card card--top">
    <h1 class="headline headline--care">Care</h1>
    <div class="badge">enough</div>
    <h1 class="headline headline--share">To Share</h1>
    <div class="fruit-art" role="img" aria-label="Illustration of a harvest fruit pile: apple, orange, lemon, bananas, grapes and pears"></div>
    <p class="season">Thanksgiving</p>
    <p class="quote">"Gratitude is not only the greatest of<br>virtues, but the parent of all others."</p>
    <p class="quote-author">— Varro Quill</p>
    <p class="offer">Who do you know who could benefit from our care? Share this message with them and we will give them a complete Consultation and Examination at no charge.</p>
  </section>

  <section class="card card--bottom">
    <h1 class="headline headline--care">Care</h1>
    <div class="badge">enough</div>
    <h1 class="headline headline--share">To Share</h1>
    <div class="fruit-art" role="img" aria-label="Illustration of a harvest fruit pile: apple, orange, lemon, bananas, grapes and pears"></div>
    <p class="season">Thanksgiving</p>
    <p class="quote">"Gratitude is not only the greatest of<br>virtues, but the parent of all others."</p>
    <p class="quote-author">— Varro Quill</p>
    <p class="offer">Who do you know who could benefit from our care? Share this message with them and we will give them a complete Consultation and Examination at no charge.</p>
  </section>
</div>
</body>
</html>
```